Webdesign for starlight path

"Der Sternpfad" is a new info product that will be selled through the website maybe you will create for us.

Translated from german to english the project is named "the starlight path". It´s an online video course that teaches people how to live a fulfilling, happy and healthy life.

Design paramaters
We want a serious design that embodies the real feeling of beeing happy and fulfilled. Visitors should even feel good/better when they see the website.
In color psychology some sort of calming deep green like a four-leaf clover is recommend.
Mainly the website will be the external sales page with a big video as the central attention.
We also need a member area for customers to watch our video course.

So mainly we need a eye-cathing, calming header, the content body with mainly video and just a few written words...and of course a footer for links like imprint, affiliate program etc.

What we not want:
- some kind of these exaggerated smiling photos
- that bathetic luck symbols like money or boats

Hi,

i posted a message to the design discussion. Thank you!

```html
<!DOCTYPE html>
<html lang="en">
<head>
<meta charset="utf-8">
<title>Der Sternpfad</title>
<link href="https://fonts.googleapis.com/css2?family=Raleway:wght@300;400&family=Open+Sans:wght@600&display=swap" rel="stylesheet">
<style>
:root{
  --header-top:#6b8a1e;
  --header-bottom:#3f5a12;
  --body-light:#a6c52a;
  --body-mid:#5f8a1f;
  --body-deep:#2b4a14;
  --button-top:#9cbf2e;
  --button-bottom:#6f9418;
  --button-text:#ffffff;
  --title-text:#e6ecd6;
  --body-text:#e4ead8;
  --player-dark:#000000;
  --player-glow:#4a4a4a;
  --controls:#f2f2f2;
  --footer-bg:#ffffff;
  --footer-text:#444444;
  --social:#3b7fc0;
  --divider:#cfe08a;
}
*{margin:0;padding:0;box-sizing:border-box}
html,body{width:1200px;height:1054px;overflow:hidden}
body{position:relative;font-family:"Raleway",sans-serif;background:var(--body-deep)}
.site-header{position:absolute;left:0;top:0;width:1200px;height:146px;
  background:linear-gradient(180deg,var(--header-top),var(--header-bottom));
  box-shadow:0 4px 10px rgba(0,0,0,.35);z-index:2}
.brand{position:absolute;left:135px;top:30px;display:flex;align-items:center;gap:22px}
.brand-mark{width:90px;height:90px;border-radius:50%;background:#e6a51c}
.brand-name{font-weight:300;font-size:42px;letter-spacing:-.5px;color:var(--title-text);text-transform:uppercase}
.header-button{position:absolute;top:53px;width:88px;height:36px;border-radius:4px;
  background:linear-gradient(180deg,var(--button-top),var(--button-bottom));
  color:var(--button-text);font-family:"Open Sans",sans-serif;font-weight:600;font-size:16px;
  display:flex;align-items:center;justify-content:center;box-shadow:0 2px 3px rgba(0,0,0,.35)}
.header-button.affiliate{left:883px}
.header-button.login{left:988px}
.sales-body{position:absolute;left:0;top:146px;width:1200px;height:791px;
  background:radial-gradient(ellipse 520px 260px at 600px 0,var(--body-light),transparent 80%),
  radial-gradient(ellipse 700px 600px at 600px 250px,var(--body-mid),var(--body-deep) 95%)}
.video-player{position:absolute;left:293px;top:49px;width:607px;height:385px;background:var(--player-dark);
  box-shadow:0 30px 25px -18px rgba(0,0,0,.55)}
.video-screen{position:absolute;inset:0 0 29px 0;
  background:radial-gradient(ellipse 320px 200px at 50% 35%,var(--player-glow),var(--player-dark) 80%)}
.video-title{position:absolute;top:130px;width:100%;text-align:center;font-weight:300;font-size:46px;
  color:#c9c9c9;text-transform:uppercase;letter-spacing:-.5px}
.play-button{position:absolute;left:268px;top:147px;width:79px;height:78px;border-radius:3px;background:rgba(170,170,170,.75)}
.video-controls{position:absolute;left:0;bottom:0;width:100%;height:29px;background:var(--controls);
  display:flex;align-items:center;font-family:"Open Sans",sans-serif;font-size:11px;color:#222}
.video-controls svg{display:block}
.time{padding:0 8px}
.track{flex:1;height:6px;background:#bdbdbd;border-radius:3px}
.buy-button{position:absolute;left:498px;top:495px;width:219px;height:47px;border-radius:4px;
  background:linear-gradient(180deg,var(--button-top),var(--button-bottom));
  color:var(--button-text);font-family:"Open Sans",sans-serif;font-weight:600;font-size:22px;
  display:flex;align-items:center;justify-content:center;box-shadow:0 2px 4px rgba(0,0,0,.35)}
.divider{position:absolute;left:100px;top:590px;width:1000px;height:1px;
  background:linear-gradient(90deg,transparent,var(--divider),transparent);opacity:.6}
.intro-text{position:absolute;left:139px;top:612px;width:920px;text-align:center;
  font-size:16.6px;line-height:23px;color:var(--body-text)}
.site-footer{position:absolute;left:0;top:937px;width:1200px;height:117px;background:var(--footer-bg)}
.copyright{position:absolute;left:125px;top:36px;font-size:14px;color:var(--footer-text)}
.social-links{position:absolute;left:859px;top:30px;display:flex}
.social-links span{width:33px;height:33px;border-radius:4px;background:var(--social);margin-right:30px}
.social-links span + span{box-shadow:-15px 0 0 -14px #ddd}
</style>
</head>
<body>
<header class="site-header">
  <div class="brand"><span class="brand-mark"></span><span class="brand-name">Der Sternpfad</span></div>
  <a class="header-button affiliate">Affliate</a>
  <a class="header-button login">Login</a>
</header>
<main class="sales-body">
  <div class="video-player">
    <div class="video-screen">
      <div class="video-title">Der Sternpfad</div>
      <div class="play-button">
        <svg width="79" height="78" viewBox="0 0 79 78"><path d="M28 22 L56 39 L28 56Z" fill="#fff"/></svg>
      </div>
    </div>
    <div class="video-controls">
      <svg width="22" height="29" viewBox="0 0 22 29"><path d="M7 10 L15 14.5 L7 19Z" fill="#111"/></svg>
      <span class="time">00:00</span>
      <span class="track"></span>
      <span class="time">00:00</span>
      <svg width="40" height="29" viewBox="0 0 40 29"><path d="M6 12h3l4-3v11l-4-3H6z" fill="#111"/><path d="M16 13v3M19 12v5M22 11v7M25 10v9M28 9v11M31 9v11" stroke="#111"/></svg>
      <svg width="24" height="29" viewBox="0 0 24 29"><path d="M7 10h4M7 10v4M17 10h-4M17 10v4M7 19h4M7 19v-4M17 19h-4M17 19v-4" stroke="#111" fill="none"/></svg>
    </div>
  </div>
  <a class="buy-button">Buy Now</a>
  <div class="divider"></div>
  <p class="intro-text">Our proposed Lumora IT Program builds on existing techniques and technologies to provide e-therapy to adults with substance abuse problems residing in five rural counties in West Texas, on the U.S.-Mexico international border.The goals of our program are to integrate the function of electronic counseling or E-Therapy capability to Verdanel's client support system. In order to improve outcomes for existing clients we proposed enhancing treatment capability and expanding treatment to remote outlying areas in the surrounding counties using technologies available in the area.</p>
</main>
<footer class="site-footer">
  <p class="copyright">© Copyright &nbsp;Der Sternpfad 2012. All Rights Reserved.</p>
  <nav class="social-links" aria-label="Social links"><span></span><span></span><span></span><span></span></nav>
</footer>
</body>
</html>
```